Business Card Design Project

I have just chosen a logo and would now like this designed onto a business card for my hair salon. I would like it to be classy not to busy and have a wow factor when people look at them
Has to Include on card:
Logo Design
And business details below
Kellie-ann Drummond (owner)
0482 736 219
Rdw@vomblet.com.au
71 Willowmere Rise Corvin Cove
Logo is now attached please provide designs
Hair

```html
<!DOCTYPE html>
<html lang="en">
<head>
<meta charset="utf-8">
<title>Velvet Lane Hair Studio – Business Card</title>
<link href="https://fonts.googleapis.com/css2?family=Didact+Gothic&display=swap" rel="stylesheet">
<style>
  :root {
    --backdrop: #dcd9d5;
    --card-white: #f1f1f0;
    --card-black: #121212;
    --brand-pink: #d4186e;
    --brand-teal: #3fb6c0;
    --ink-light: #ffffff;
  }
  * { margin: 0; padding: 0; box-sizing: border-box; }
  html, body {
    width: 1200px;
    height: 1076px;
    overflow: hidden;
    background: var(--backdrop);
    font-family: "Didact Gothic", "Century Gothic", sans-serif;
  }
  .business-card {
    position: absolute;
    left: 100px;
    top: 238px;
    width: 1000px;
    height: 600px;
    background: var(--card-white);
    overflow: hidden;
    box-shadow: 0 12px 30px rgba(0,0,0,0.25);
  }
  .card-shape {
    position: absolute;
    inset: 0;
    width: 1000px;
    height: 600px;
  }
  .card-shape .black-sweep { fill: var(--card-black); }
  .brand-mark {
    position: absolute;
    left: 470px;
    top: 70px;
    display: flex;
    align-items: center;
    gap: 18px;
  }
  .brand-dot {
    width: 26px;
    height: 26px;
    border-radius: 50%;
    background: var(--brand-teal);
    flex: none;
  }
  .brand-name {
    color: var(--brand-pink);
    font-size: 52px;
    line-height: 1.05;
    letter-spacing: 1px;
    text-transform: uppercase;
  }
  .contact-details {
    position: absolute;
    right: 40px;
    top: 330px;
    list-style: none;
    text-align: right;
    color: var(--ink-light);
    font-size: 31px;
    line-height: 46px;
    letter-spacing: 0.5px;
  }
  .contact-details .owner-name { font-size: 29px; }
</style>
</head>
<body>
  <section class="business-card">
    <svg class="card-shape" viewBox="0 0 1000 600" aria-hidden="true">
      <path class="black-sweep" d="M0,240 C260,225 480,300 630,300 C810,300 930,170 1000,25 L1000,555 L0,555 Z"/>
    </svg>

    <div class="brand-mark">
      <span class="brand-dot"></span>
      <h1 class="brand-name">Velvet Lane<br>Hair Studio</h1>
    </div>

    <ul class="contact-details">
      <li class="owner-name">Kellie-ann Drummond (owner)</li>
      <li class="phone">0482 736 219</li>
      <li class="email">Rdw@vomblet.com.au</li>
      <li class="address">71 Willowmere Rise Corvin Cove</li>
    </ul>
  </section>
</body>
</html>
```